Wine bottle label design

I'm looking for assistance designing a front and back label for a private wine collection. Please could you use the attached drawing from my daughter as a reference to propose a front label design for the wine bottle label? Feel free to be creative, the label is Seven owls - see explanation below
Back label wording
7 Owls  was created in 2011 by 3 friends with a great passion for Napa Cabernets.  The  grapes were sourced in Napa Valley, California and cleaned and pressed in Houston, Texas by 11 family members to create 7 Owls according to the time honored tradition of the Dorn/Montaubrey/Pellow  winemakers.  Aged for 18 months in a new “Toasted French Oak Barrel” and racked monthly by our friends at Barrelmark Co.  Cheers to all our family members  for helping to produce this very high quality wine, with a soft, elegant, yet ripe and rich quality.  This wine is abundant in textural tannins yet soft as velvet.
Winemakers: the original DMPs : Gavin Dorn, Ferdinand Montaubrey, Paul Pellow
Region: Napa
State: California Grapes aged in Texas
acl by vol: 13.5% Alcohol by volume

Target Market(s)
will be used to drink socially and give as gifts to friends.
Wine is Red and should indicate the following on the front label (as all wines):
Year :  2011
Cabernet Sauvignon
Requirements
Nice to have
- try to incoporate a Cat or "cats" similar to the design my daughter skectched if possible
feel free to improve the design of the number "11"
some form of simple design around the back label would also be nice - see wording above

```html
<!DOCTYPE html>
<html lang="en">
<head>
<meta charset="utf-8">
<title>Seven Owls – Wine Labels</title>
<link rel="stylesheet" href="https://fonts.googleapis.com/css2?family=Oswald:wght@300;400;500&family=Montserrat:wght@400;600;700&display=swap">
<style>
  :root {
    --stage-dark: #0d0b0b;
    --stage-mid: #3a3634;
    --label-black: #050505;
    --label-red: #e4161f;
    --label-red-deep: #b80f16;
    --gold: #b8872f;
    --gold-soft: #c79b42;
    --white: #ffffff;
    --green: #7cc242;
    --accent-red: #e8202a;
  }
  * { margin: 0; padding: 0; box-sizing: border-box; }
  html, body { width: 1200px; height: 1000px; overflow: hidden; }
  body {
    position: relative;
    background: radial-gradient(ellipse 60% 70% at 40% 20%, var(--stage-mid), var(--stage-dark) 75%);
    font-family: "Oswald", sans-serif;
  }

  /* ---------- Front label ---------- */
  .front-label {
    position: absolute;
    left: 130px; top: 64px;
    width: 419px; height: 879px;
    background: linear-gradient(to bottom,
      var(--label-red) 0%, var(--label-red) 40%,
      var(--label-red-deep) 52%, var(--label-black) 64%, var(--label-black) 100%);
    overflow: hidden;
  }
  .label-frame { position: absolute; }
  .front-label .label-frame { left: 22px; top: 22px; }
  .cat-artwork {
    position: absolute;
    left: 100px; top: 40px;
    width: 220px; height: 450px;
    border-radius: 45% 45% 40% 40%;
    background: radial-gradient(ellipse at 50% 55%, #0a0a0a 0%, #151010 55%, rgba(20,10,10,0) 72%);
  }
  .wine-name {
    position: absolute;
    left: 0; width: 100%;
    text-align: center;
    color: var(--white);
    font-family: "Oswald", sans-serif;
    font-weight: 500;
    line-height: 1;
  }
  .front-label .wine-name-line1 { top: 418px; font-size: 150px; letter-spacing: -2px; }
  .front-label .wine-name-line2 { top: 568px; font-size: 150px; letter-spacing: -2px; }
  .rule {
    position: absolute;
    height: 1px;
    background: var(--gold);
  }
  .front-label .rule-top { left: 50px; width: 318px; top: 720px; }
  .front-label .rule-bottom { left: 50px; width: 318px; top: 765px; }
  .varietal {
    position: absolute;
    left: 0; width: 100%; top: 728px;
    text-align: center;
    font-family: "Montserrat", sans-serif;
    font-weight: 400;
    font-size: 23px;
    letter-spacing: 1px;
    color: var(--green);
  }
  .vintage-line {
    position: absolute;
    left: 0; width: 100%; top: 778px;
    text-align: center;
    color: var(--white);
    font-size: 16px;
    white-space: nowrap;
  }
  .vintage-line .year { font-family: "Montserrat", sans-serif; font-weight: 600; letter-spacing: 1px; }
  .vintage-line .region {
    font-family: "Oswald", sans-serif; font-weight: 400; font-size: 19px;
    color: var(--accent-red); letter-spacing: 1px; margin: 0 8px;
  }
  .vintage-line .abv { font-family: "Montserrat", sans-serif; font-weight: 400; font-size: 15px; }
  .origin-note {
    position: absolute;
    left: 0; width: 100%; top: 807px;
    text-align: center;
    font-family: "Montserrat", sans-serif;
    font-weight: 700;
    font-size: 11.5px;
    line-height: 17px;
    letter-spacing: 1px;
    color: var(--gold-soft);
  }

  /* ---------- Back label ---------- */
  .back-label {
    position: absolute;
    left: 676px; top: 232px;
    width: 439px; height: 544px;
    background: var(--label-black);
  }
  .back-label .label-frame { left: 12px; top: 12px; }
  .back-label .wine-name { font-size: 64px; letter-spacing: -1px; }
  .back-label .wine-name-line1 { top: 22px; }
  .back-label .wine-name-line2 { top: 86px; }
  .back-label .rule-top { left: 30px; width: 379px; top: 159px; }
  .back-label .rule-bottom { left: 30px; width: 379px; top: 470px; }
  .story {
    position: absolute;
    left: 22px; width: 395px; top: 172px;
    text-align: center;
    font-family: "Oswald", sans-serif;
    font-weight: 300;
    font-size: 16px;
    line-height: 23.5px;
    letter-spacing: 0.2px;
    color: var(--white);
  }
  .winemakers {
    position: absolute;
    left: 0; width: 100%; top: 484px;
    text-align: center;
    font-family: "Montserrat", sans-serif;
    font-weight: 700;
    font-size: 11px;
    line-height: 18px;
    letter-spacing: 0.8px;
  }
  .winemakers .winemakers-title { color: var(--accent-red); }
  .winemakers .winemakers-names { color: var(--gold-soft); }
</style>
</head>
<body>

  <section class="front-label">
    <div class="cat-artwork" role="img" aria-label="Illustration of a black seated cat with green eye and red line accents, shown in profile"></div>

    <svg class="label-frame" width="375" height="836" viewBox="0 0 375 836" aria-hidden="true">
      <path d="M28,2 H347 A26 26 0 0 0 373,28 V808 A26 26 0 0 0 347,834 H28 A26 26 0 0 0 2,808 V28 A26 26 0 0 0 28,2 Z"
            fill="none" stroke="#b8872f" stroke-width="3"/>
    </svg>

    <div class="wine-name wine-name-line1">SEVEN</div>
    <div class="wine-name wine-name-line2">OWLS</div>

    <div class="rule rule-top"></div>
    <div class="varietal">CABERNET SAUVIGNON</div>
    <div class="rule rule-bottom"></div>

    <div class="vintage-line">
      <span class="year">2011</span><span class="region">NAPA VALLEY</span><span class="abv">13%vol.</span>
    </div>
    <div class="origin-note">CALIFORNIA GRAPES<br>AGED IN TEXAS</div>
  </section>

  <section class="back-label">
    <svg class="label-frame" width="415" height="520" viewBox="0 0 415 520" aria-hidden="true">
      <path d="M40,1 H375 A39 39 0 0 0 414,40 V500 A19 19 0 0 0 395,519 H20 A19 19 0 0 0 1,500 V40 A39 39 0 0 0 40,1 Z"
            fill="none" stroke="#b8872f" stroke-width="1.2"/>
    </svg>

    <div class="wine-name wine-name-line1">SEVEN</div>
    <div class="wine-name wine-name-line2">OWLS</div>

    <div class="rule rule-top"></div>
    <p class="story">7 Owls was created in 2011 by 3 friends with a great passion for Napa Cabernets. The grapes were sourced in Napa Valley, California and cleaned and pressed in Houston, Texas by 11 family members to create 7 Owls according to the time honored tradition of the Dorn/Montaubrey/Pellow winemakers. Aged for 18 months in a new “Toasted French Oak Barrel” and racked monthly by our friends at Barrelmark Co. Cheers to all our family members for helping to produce this very high quality wine, with a soft, elegant, yet ripe and rich quality. This wine is abundant in textural tannins yet soft as velvet.</p>
    <div class="rule rule-bottom"></div>

    <div class="winemakers">
      <div class="winemakers-title">WINEMAKERS (THE ORIGINAL DMPS)</div>
      <div class="winemakers-names">GAVIN DORN, FERDINAND MONTAUBREY, PAUL PELLOW</div>
    </div>
  </section>

</body>
</html>
```